Menu Design Project for New Catering company

I would like to see my menus in a warm, inviting format. I prepare food for small intimate dinners, business lunches, picnics, parties, weddings and rehearsal dinners. I work with clients to help create their dream whether it includes items on my menu or to prepare very personal dishes that bring them warm memories of a special time or moment.

Target Market(s)

Organizations, wedding and or event planners

Industry/Entity Type

Catering

Requirements
Must have
• I would like to include the logo that is included in the attachment below. I also included a copy of the poster Lex Doyle created for me. I hope this helps. Please be creative. I am a very happy, cheerful person that enjoys cooking and having fun. I would like the design to represent my personality as well as my food. When I cater I treat my customers like an extension of my family and it comes across to them with everything I do for them. I hope this can somehow be reflected in your designs.
Should not have
• I'm open to all ideas and don't want to limit your creativity.

```html
<!DOCTYPE html>
<html lang="en">
<head>
<meta charset="utf-8">
<title>Box Lunches Menu – Bright Basil Catering</title>
<link href="https://fonts.googleapis.com/css2?family=Open+Sans:wght@400;600;700;800&family=PT+Sans:wght@400;700&display=swap" rel="stylesheet">
<style>
  :root {
    --green: #3aaa48;
    --green-deep: #2f9a3f;
    --band-top: #4fae58;
    --band-bottom: #3f9f49;
    --ink: #111;
    --brand-grey: #58585a;
    --white: #fff;
  }
  * { margin: 0; padding: 0; box-sizing: border-box; }
  html, body { width: 1200px; height: 729px; overflow: hidden; background: var(--white); }
  body { position: relative; font-family: "Open Sans", Arial, sans-serif; color: var(--ink); }

  .side-panel { position: absolute; top: 0; width: 301px; height: 729px; overflow: hidden; }
  .side-panel--left { left: 0; }
  .side-panel--right { left: 899px; }

  .brand-mark { position: absolute; top: 78px; width: 112px; height: 112px; border: 7px solid var(--green-deep); border-radius: 50%; }
  .side-panel--left .brand-mark { left: -46px; }
  .side-panel--right .brand-mark { left: 226px; }

  .brand-name { position: absolute; top: 203px; font-weight: 700; font-size: 34px; color: var(--brand-grey); white-space: nowrap; letter-spacing: -0.5px; }
  .side-panel--left .brand-name { right: 149px; }
  .side-panel--right .brand-name { left: 148px; }

  .food-photo { position: absolute; left: 0; top: 300px; width: 301px; height: 429px;
    background: linear-gradient(170deg, var(--band-top) 0%, #58b25e 45%, var(--band-bottom) 100%); }

  .contact { position: absolute; color: var(--white); font-weight: 700; white-space: nowrap; }
  .contact__phone { font-size: 25px; top: 637px; }
  .contact__web { font-size: 13.5px; top: 670px; }
  .side-panel--left .contact { right: 218px; text-align: right; }
  .side-panel--right .contact { left: 217px; }
  .side-panel--right .contact__web { left: 179px; }

  .menu-panel { position: absolute; left: 301px; top: 0; width: 598px; height: 729px; background: var(--white); }
  .menu-photo { position: absolute; left: 0; top: 150px; width: 598px; height: 579px;
    background: linear-gradient(180deg, #ffffff 0%, #f6f3ee 30%, #f1e8dc 60%, #ece3d8 100%); }

  .menu-title { position: absolute; left: 20px; top: 58px; font-size: 41px; font-weight: 800; color: var(--green); letter-spacing: 0.3px; }
  .menu-intro { position: absolute; left: 20px; top: 111px; font-family: "PT Sans", Arial, sans-serif; font-size: 14.2px; line-height: 18px; white-space: nowrap; }
  .menu-intro b { font-weight: 700; }
  .menu-price { position: absolute; left: 307px; top: 150px; font-family: "PT Sans", Arial, sans-serif; font-size: 11.5px; font-weight: 700; white-space: nowrap; }
  .menu-price sup { font-size: 8px; }
  .menu-price .price-big { font-size: 14px; }
  .menu-price .note { font-weight: 400; }

  .menu-items { position: absolute; left: 20px; top: 0; width: 276px; }
  .menu-item { position: absolute; left: 0; width: 276px; }
  .menu-item__name { font-size: 13px; font-weight: 700; line-height: 16px; letter-spacing: 0.2px; }
  .menu-item__desc { font-family: "PT Sans", Arial, sans-serif; font-size: 10.3px; line-height: 13px; margin-top: 1px; }

  .menu-extras { position: absolute; left: 306px; width: 290px; }
  .extra { position: absolute; left: 0; width: 270px; }
  .extra__title { font-size: 10.5px; font-weight: 700; letter-spacing: 0.2px; }
  .extra__title sup { font-size: 7px; }
  .extra__text { font-family: "PT Sans", Arial, sans-serif; font-size: 10.3px; line-height: 13px; }
  .extra__text sup { font-size: 7px; font-weight: 700; }

  .menu-web { position: absolute; left: 320px; top: 672px; font-size: 13.5px; font-weight: 700; color: var(--green); white-space: nowrap; }
</style>
</head>
<body>

  <aside class="side-panel side-panel--left">
    <div class="brand-mark"></div>
    <div class="brand-name">Bright Basil Catering</div>
    <div class="food-photo" role="img" aria-label="Photo of a green catering spread with broccoli and salads"></div>
    <div class="contact contact__phone">812.555.0142</div>
    <div class="contact contact__web">www.brightbasilcatering.com</div>
  </aside>

  <main class="menu-panel">
    <div class="menu-photo" role="img" aria-label="Faded photo of kraft box lunches tied with ribbon on a table"></div>

    <h1 class="menu-title">BOX LUNCHES</h1>
    <p class="menu-intro">Served with choice of <b>chips, fruit cup or side house salad</b> and choice of <b>cookie or cupcake</b>.<br>Drinks sold separately.&nbsp; Price per lunch for orders of 10 or more to a single location.</p>
    <p class="menu-price"><span class="price-big"><sup>$</sup>9<sup>00</sup></span> plus tax each <span class="note">(*no delivery fee)</span></p>

    <section class="menu-items">
      <div class="menu-item" style="top:193px">
        <h2 class="menu-item__name">MALIBU CHICKEN</h2>
        <p class="menu-item__desc">Grilled chicken breast, topped with sweet honey baked ham, Swiss cheese and served on a fresh croissant with a side of rich sweet mustard sauce.</p>
      </div>
      <div class="menu-item" style="top:259px">
        <h2 class="menu-item__name">ITALIAN MEATBALL WITH<br>MOZZARELLA CHEESE</h2>
        <p class="menu-item__desc">In a rich marinara sauce served on a fresh Hoagie Bun.</p>
      </div>
      <div class="menu-item" style="top:315px">
        <h2 class="menu-item__name">GRILLED HAWAIIAN CHICKEN SANDWICH</h2>
        <p class="menu-item__desc">Grilled chicken topped with a sweet grilled pineapple ring and guacamole sauce on a fresh Hawaiian bun or croissant.</p>
      </div>
      <div class="menu-item" style="top:371px">
        <h2 class="menu-item__name">HONEY CHICKEN SALAD</h2>
        <p class="menu-item__desc">A fresh mayo-free chicken salad filled with grapes, crispy celery, pecans, shredded chicken mixed with a light dressing of plain Greek yogurt, honey and Dijon mustard - served on a fresh croissant.</p>
      </div>
      <div class="menu-item" style="top:455px">
        <h2 class="menu-item__name">HONEY BAKED HAM &amp; SWISS CHEESE</h2>
        <p class="menu-item__desc">Piled high on a fresh croissant (with choices of - lettuce, tomato slice, onions and mayo/salad dressing).</p>
      </div>
      <div class="menu-item" style="top:510px">
        <h2 class="menu-item__name">ULTIMATE BLT WITH AVOCADO AND<br>SPICY MAYO</h2>
        <p class="menu-item__desc">Crispy bacon, lettuce, tomato, thin slices of red onion, avocado slices atop toasted bread with spicy mayo.</p>
      </div>
      <div class="menu-item" style="top:585px">
        <h2 class="menu-item__name">SPINACH SALAD&nbsp; WITH BACON DRESSING</h2>
        <p class="menu-item__desc">Baby Spinach, mushrooms, red onions and sliced boiled eggs served with croissant and bacon dressing.</p>
      </div>
    </section>

    <section class="menu-extras">
      <div class="extra" style="top:194px">
        <h3 class="extra__title">SALAD DRESSING CHOICES</h3>
        <p class="extra__text">Ranch, Italian, Honey Mustard or Blue Cheese</p>
      </div>
      <div class="extra" style="top:240px">
        <h3 class="extra__title">DRINKS - <sup>$</sup>1<sup>00</sup> each</h3>
        <p class="extra__text">12 oz. soft drinks<br>16 oz. bottled water</p>
      </div>
      <div class="extra" style="top:293px">
        <p class="extra__text">* A delivery fee of <b><sup>$</sup>2<sup>00</sup> each</b> for orders totaling less than 10 box lunches</p>
      </div>
    </section>

    <p class="menu-web">www.brightbasilcatering.com</p>
  </main>

  <aside class="side-panel side-panel--right">
    <div class="brand-mark"></div>
    <div class="brand-name">Bright Basil Catering</div>
    <div class="food-photo" role="img" aria-label="Photo of a green catering spread with plated appetizers"></div>
    <div class="contact contact__phone">812.555.0142</div>
    <div class="contact contact__web">www.brightbasilcatering.com</div>
  </aside>

</body>
</html>
```